Double caffeinated coffee label design

We need to design labels for a new coffee brand. The label size: 2.75” x 4.125” (Corners slightly rounded). There will be front and back label in stickers to be put on standardized bags. Our product is roasted whole bean and ground coffee in 12oz bags. It is described as "strong, bold, intense, and double caffeinated. The product is designed for passionate coffee drinkers who want strong, more caffeinated but not bitter coffee. The coffee is suitable for espresso base coffees.
Target Market(s)
Groceries, food stores, super markets. Heavy and sophisticated coffee drinkers.
Requirements
Must have
- Modern, minimalist style. Strong and bold look. Creative. Impressive.
Nice to have
- Some impressed coffee label designs for reference: https://www.vistrelo.net/find?q=most+impressive+coffee+brand+designs&src=menu&mode=img&ref=X&key=7hQpLmZrT2wXvBn4KcYsDfGaJuEo9RtMiHb3NqVe&w=1280&h=610#pic=kR4mTwXzNpQbLs:

```html
<!DOCTYPE html>
<html lang="en">
<head>
<meta charset="utf-8">
<title>Velorn Coffee – Front Label</title>
<link href="https://fonts.googleapis.com/css2?family=Oswald:wght@500;600&family=Montserrat:wght@400;500&display=swap" rel="stylesheet">
<style>
  :root {
    --page: #ffffff;
    --label-red: #dc2e12;
    --label-red-light: #f1603f;
    --label-red-deep: #c92008;
    --band: #ececea;
    --ink: #262626;
    --ink-red: #5b1c10;
    --brand-grey: #dcdcdc;
  }
  * { margin: 0; padding: 0; box-sizing: border-box; }
  html, body {
    width: 1200px; height: 1200px; overflow: hidden;
    background: var(--page);
  }
  .canvas { position: relative; width: 1200px; height: 1200px; }
  .label {
    position: absolute; left: 244px; top: 96px;
    width: 712px; height: 1008px;
    border-radius: 14px; overflow: hidden;
    background: linear-gradient(90deg, var(--label-red-light) 0%, var(--label-red) 30%, var(--label-red-deep) 55%, var(--label-red) 80%, var(--label-red-light) 100%);
    text-align: center;
    font-family: "Montserrat", sans-serif;
  }
  .brand {
    position: absolute; left: 0; right: 0; top: 88px;
    display: flex; justify-content: center; align-items: center; gap: 18px;
  }
  .brand-dot {
    width: 26px; height: 26px; border-radius: 50%;
    background: var(--brand-grey);
  }
  .brand-name {
    font-family: "Montserrat", sans-serif; font-weight: 500;
    font-size: 104px; line-height: 1; color: var(--brand-grey);
    letter-spacing: 1px;
  }
  .brand-sub {
    position: absolute; left: 0; right: 0; top: 228px;
    font-size: 34px; letter-spacing: 6px; color: var(--brand-grey);
    padding-left: 90px;
  }
  .band { position: absolute; left: 0; top: 326px; width: 712px; height: 386px; }
  .title {
    position: absolute; left: 0; right: 0; top: 386px;
    font-family: "Oswald", sans-serif; font-weight: 600;
    font-size: 156px; line-height: 1; color: var(--ink);
    letter-spacing: -3px; transform: scaleX(0.86);
  }
  .subtitle {
    position: absolute; left: 0; right: 0; top: 556px;
    font-family: "Oswald", sans-serif; font-weight: 600;
    font-size: 70px; line-height: 1; color: var(--ink);
    letter-spacing: -1px; transform: scaleX(0.86);
  }
  .format {
    position: absolute; left: 0; right: 0; top: 644px;
    font-size: 30px; letter-spacing: 3px; color: var(--ink);
    word-spacing: 14px;
  }
  .tagline {
    position: absolute; left: 122px; top: 754px; width: 458px; height: 56px;
    border: 2px solid var(--ink);
    font-size: 27px; line-height: 52px; letter-spacing: 2px;
    color: var(--ink);
  }
  .strength {
    position: absolute; left: 0; right: 0; top: 836px;
    font-size: 22px; letter-spacing: 7px; word-spacing: 18px;
    color: var(--ink-red);
  }
  .weight {
    position: absolute; left: 0; right: 0; top: 884px;
    font-size: 33px; letter-spacing: 4px; color: var(--ink);
  }
</style>
</head>
<body>
<main class="canvas">
  <section class="label">
    <div class="brand">
      <span class="brand-dot"></span>
      <span class="brand-name">Velorn</span>
    </div>
    <div class="brand-sub">COFFEE</div>

    <svg class="band" viewBox="0 0 712 386" preserveAspectRatio="none" aria-hidden="true">
      <path fill="#ececea" d="M0 14 L40 8 L90 12 L140 4 L200 10 L250 6 L310 12 L370 5 L430 11 L490 6 L560 12 L620 4 L680 10 L712 7
        L712 372 L670 378 L610 370 L560 380 L500 372 L440 379 L380 371 L320 378 L260 370 L200 380 L140 371 L80 378 L30 372 L0 376 Z"/>
    </svg>

    <h1 class="title">ROASTED</h1>
    <h2 class="subtitle">WHOLE BEAN</h2>
    <p class="format">★ GROUND COFFEE ★</p>

    <p class="tagline">STRONG, BOLD, INTENSE</p>
    <p class="strength">DOUBLE CAFFEINATED</p>
    <p class="weight">12 oz</p>
  </section>
</main>
</body>
</html>
```